Orbit 582 - Kindle Book Cover

I am looking for a Kindle book cover for my book about "Orbit 582".
The Book is Titled:
Orbit 582 Ascended
Shaping Tomorrow: Paths To Unlocking Hidden Currents
Author is Dorian Welby
Here is a book description that may help you understand more about it:
Inspired by the genius of Bertram Ollinger, this comprehensive guide delves into the ancient wisdom and cutting-edge science behind the 582 method, a powerful tool for manifesting your desires. Whether you're seeking personal growth, financial success, or spiritual enlightenment, this book provides advanced techniques and methods to transform your dreams into reality.
Any questions please ask.
Thanks
Gavin

```html
<!DOCTYPE html>
<html lang="en">
<head>
<meta charset="utf-8">
<title>Orbit 582 Ascended — Dorian Welby</title>
<link rel="stylesheet" href="https://fonts.googleapis.com/css2?family=Montserrat:wght@300;400;700;800&family=Poppins:wght@600;700&display=swap">
<style>
  :root {
    --sky-top: #23272e;
    --sky-mid: #5d6269;
    --sky-low: #7a7e84;
    --sky-bottom: #3f4348;
    --city-dark: #1c1d22;
    --city-warm: #5a2a2c;
    --city-light: #b8463f;
    --author-pink: #f4ddd3;
    --title-yellow: #fde58a;
    --number-blue: #e4f2fc;
    --text-white: #ffffff;
  }
  * { margin: 0; padding: 0; box-sizing: border-box; }
  html, body { width: 805px; height: 1200px; overflow: hidden; background: var(--sky-top); }
  .cover {
    position: relative;
    width: 805px;
    height: 1200px;
    overflow: hidden;
    font-family: "Montserrat", sans-serif;
  }
  .backdrop {
    position: absolute; inset: 0;
    background: linear-gradient(180deg, var(--sky-top) 0%, #3b3f46 25%, var(--sky-mid) 55%, var(--sky-low) 72%, var(--sky-bottom) 100%);
  }
  .figure-scene {
    position: absolute;
    left: 300px; top: 120px;
    width: 505px; height: 1080px;
    border-radius: 170px 170px 0 0;
    background:
      linear-gradient(180deg, rgba(70,74,82,0.55) 0%, rgba(60,62,70,0.6) 38%, rgba(40,38,44,0.9) 55%, var(--city-dark) 70%, var(--city-warm) 85%, var(--city-light) 100%);
  }
  .author {
    position: absolute;
    top: 58px; left: 0; width: 805px;
    text-align: center;
    font-family: "Montserrat", sans-serif;
    font-weight: 300;
    font-size: 50px;
    letter-spacing: 17px;
    color: var(--author-pink);
  }
  .title-word {
    position: absolute;
    left: 96px; top: 340px;
    font-family: "Poppins", sans-serif;
    font-weight: 700;
    font-size: 80px;
    letter-spacing: -3px;
    line-height: 1;
    color: var(--title-yellow);
  }
  .title-number {
    position: absolute;
    left: 98px; top: 400px;
    font-family: "Poppins", sans-serif;
    font-weight: 600;
    font-size: 270px;
    letter-spacing: -6px;
    line-height: 1;
    color: var(--number-blue);
    text-shadow: 0 4px 10px rgba(0,0,0,0.25);
  }
  .title-edition {
    position: absolute;
    left: 92px; top: 655px;
    font-family: "Montserrat", sans-serif;
    font-weight: 800;
    font-size: 48px;
    letter-spacing: 20px;
    line-height: 1;
    color: var(--text-white);
  }
  .subtitle {
    position: absolute;
    left: 60px; top: 880px;
    width: 300px;
    color: var(--text-white);
    font-weight: 400;
  }
  .subtitle-lead {
    font-size: 29px;
    line-height: 37px;
    text-transform: uppercase;
  }
  .subtitle-body {
    margin-top: 22px;
    font-size: 29px;
    line-height: 37px;
  }
</style>
</head>
<body>
  <main class="cover">
    <div class="backdrop" role="img" aria-label="Overcast grey sky background"></div>
    <div class="figure-scene" role="img" aria-label="Silhouette of a woman in a suit blended with a city street and red light trails at dusk"></div>

    <p class="author">DORIAN WELBY</p>

    <h1 class="title">
      <span class="title-word">ORBIT</span>
      <span class="title-number">582</span>
      <span class="title-edition">ASCENDED</span>
    </h1>

    <div class="subtitle">
      <p class="subtitle-lead">Shaping<br>Tomorrow:</p>
      <p class="subtitle-body">Paths to<br>unlocking<br>hidden currents</p>
    </div>
  </main>
</body>
</html>
```